Boutique Technology Consultancy specialising is Electronic and physical security

We need to redo our existing outdated website. For your reference the link www.brivo.com.au

```html
<!DOCTYPE html>
<html lang="en">
<head>
<meta charset="utf-8">
<title>Kelvarn Services</title>
<link href="https://fonts.googleapis.com/css2?family=Roboto:wght@400;500;700;900&display=swap" rel="stylesheet">
<style>
:root{
  --red:#e0231f;
  --black:#070707;
  --panel:#0f0f0f;
  --card:#121212;
  --white:#ffffff;
  --muted:#d8d8d8;
}
*{box-sizing:border-box;margin:0;padding:0}
html,body{width:1200px;height:3779px;overflow:hidden;background:var(--black);font-family:'Roboto',Arial,sans-serif;color:var(--white)}
.page{position:relative;width:1200px;height:3779px;overflow:hidden}
.abs{position:absolute}
.top-rule{left:0;top:0;width:1200px;height:4px;background:var(--red)}
.brand{display:flex;align-items:center;gap:12px;font-weight:700;color:var(--white);letter-spacing:1px;white-space:nowrap}
.brand-mark{background:var(--red);display:block;flex:none}
.nav{top:56px;left:424px;font-size:15px;font-weight:700}
.nav a{position:absolute;white-space:nowrap;color:var(--white);text-decoration:none}
.nav a.active{color:var(--red)}
.btn-outline{border:2px solid var(--red);color:var(--white);font-weight:700;font-size:14px;display:flex;align-items:center;justify-content:center;text-transform:uppercase}
.btn-solid{background:var(--red);color:var(--white);font-weight:700;font-size:14px;display:flex;align-items:center;justify-content:center}
.hero-photo{left:0;top:128px;width:1200px;height:635px;background:linear-gradient(100deg,#0d1d2c 0%,#1d3a55 30%,#2b4258 55%,#1a2330 80%,#0c0f14 100%)}
.hero-frame{left:111px;top:220px;width:280px;height:294px;border-left:5px solid var(--white);border-top:5px solid var(--white)}
.hero-title{left:151px;top:258px;font-size:45px;font-weight:900;line-height:53px;text-transform:uppercase;width:390px}
.section-title{width:1200px;left:0;text-align:center;font-size:45px;font-weight:900;text-transform:uppercase}
.section-title span,.about-title span{color:var(--red)}
.service-card{top:962px;width:257px;height:360px;display:flex;align-items:flex-end;justify-content:center;padding-bottom:20px;font-size:18px;font-weight:700;text-transform:uppercase}
.about{left:0;top:1501px;width:1200px;height:481px;background:var(--panel)}
.about-title{left:111px;top:1563px;font-size:36px;font-weight:900;text-transform:uppercase}
.about-text{left:111px;top:1640px;width:456px;font-size:14px;line-height:25.7px;text-align:justify;color:var(--white)}
.about-text p+p{margin-top:15px}
.exp-intro{left:0;width:1200px;top:2177px;text-align:center;font-size:17px;line-height:28px;color:var(--white)}
.exp-card{top:2268px;width:300px;height:402px;background:var(--card);text-align:center}
.exp-card.current{border-bottom:4px solid var(--red)}
.exp-img{margin:9px 9px 0;height:196px}
.exp-card h3{margin-top:26px;font-size:17px;font-weight:700;text-transform:uppercase}
.exp-card p{margin:22px 10px 0;font-size:15px;line-height:26px;color:var(--muted);white-space:nowrap}
.arrow{top:2454px;width:20px;height:30px}
.contact{left:0;top:2814px;width:1200px;height:680px;background:radial-gradient(circle at 50% 30%,#e8322c 0%,#d81f1b 45%,#b8110f 100%)}
.field{background:var(--white);color:#777;font-size:14px;padding:0 16px;display:flex;align-items:center;border-radius:2px}
.field.area{align-items:flex-start;padding-top:14px}
.submit{left:530px;top:3196px;width:140px;height:45px;background:var(--black);font-size:14px;font-weight:700;display:flex;align-items:center;justify-content:center}
.foot-head{top:3487px;font-size:17px;font-weight:700;text-transform:uppercase}
.foot-link{font-size:14px;display:flex;align-items:center;gap:16px;text-transform:uppercase}
.dot{width:12px;height:12px;border-radius:50%;background:var(--red);position:relative;flex:none}
.dot::after{content:"";position:absolute;left:4px;top:4px;border-left:5px solid var(--black);border-top:2px solid transparent;border-bottom:2px solid transparent}
.info-label{font-size:14px;font-weight:700;text-transform:uppercase}
.info-text{font-size:11px;line-height:21px;text-transform:uppercase}
.divider{left:111px;top:3723px;width:976px;height:1px;background:#333}
.copyright{left:0;width:1200px;top:3742px;text-align:center;font-size:13px}
</style>
</head>
<body>
<div class="page">

  <div class="abs top-rule"></div>
  <div class="abs brand" style="left:110px;top:38px;font-size:42px;">
    <span class="brand-mark" style="width:36px;height:36px"></span>KELVARN
  </div>
  <nav class="abs nav">
    <a class="active" style="left:0">HOME</a>
    <a style="left:70px">EXPERIENCE</a>
    <a style="left:185px">SERVICES</a>
    <a style="left:280px">TEAM</a>
    <a style="left:349px">ABOUT</a>
    <a style="left:425px">CONTACT</a>
  </nav>
  <div class="abs btn-outline" style="left:952px;top:44px;width:135px;height:44px">GET A QUOTE</div>

  <div class="abs hero-photo" role="img" aria-label="Two consultants reviewing a tablet in a server room"></div>
  <svg class="abs" style="left:0;top:128px" width="1200" height="635" viewBox="0 0 1200 635">
    <polygon points="0,470 705,618 690,635 0,510" fill="#e0231f"/>
    <polygon points="0,510 690,635 0,635" fill="#070707"/>
    <polygon points="690,635 1200,560 1200,635" fill="#070707"/>
  </svg>
  <div class="abs hero-frame"></div>
  <h1 class="abs hero-title">Your<br>technology<br>projects made<br>easy.</h1>
  <div class="abs btn-solid" style="left:151px;top:491px;width:137px;height:44px">GET STARTED</div>

  <h2 class="abs section-title" style="top:864px"><span>Our</span> Services</h2>
  <div class="abs service-card" style="left:43px;background:linear-gradient(180deg,#1a2433,#3a2a22 60%,#131820)" role="img" aria-label="City skyline at night with connected lights">Smart Buildings</div>
  <div class="abs service-card" style="left:329px;background:linear-gradient(160deg,#6a6c6e,#2b3a55 50%,#0e1e3a)" role="img" aria-label="Hands on a laptop with network graphic">Systems Integration</div>
  <div class="abs service-card" style="left:615px;background:linear-gradient(180deg,#1a6f8a,#0f3548 55%,#101418)" role="img" aria-label="Operator in a control room with screens">Control Centres</div>
  <div class="abs service-card" style="left:899px;background:linear-gradient(180deg,#a6b8c8,#4b6f8f 55%,#1f3f5e)" role="img" aria-label="Security cameras on a tower">CCTV</div>
  <div class="abs btn-outline" style="left:510px;top:1369px;width:179px;height:47px">View All Services</div>

  <section class="abs about"></section>
  <svg class="abs" style="left:0;top:1501px" width="1200" height="481" viewBox="0 0 1200 481">
    <polygon points="557,0 572,0 760,481 720,481" fill="#e0231f"/>
  </svg>
  <div class="abs" style="left:572px;top:1501px;width:628px;height:481px;clip-path:polygon(0 0,100% 0,100% 100%,30% 100%);background:linear-gradient(110deg,#1c2c3c,#3f6b8f 60%,#6a98c0)" role="img" aria-label="Two engineers checking a tablet beside server racks"></div>
  <h2 class="abs about-title"><span>About</span> Us</h2>
  <div class="abs about-text">
    <p>In 2022, Kelvarn Services merged Tarrowind Systems Group into its operations, bringing increased capacity and capability to the NSW office.</p>
    <p>Kelvarn is a privately owned independent consultancy 100% dedicated to customer satisfaction. With experience in a range of technologies such as internet of things, security systems, wi-fi, building services networks, control centres and smart buildings, our services include</p>
  </div>
  <div class="abs btn-outline" style="left:111px;top:1864px;width:146px;height:46px">Learn More</div>

  <h2 class="abs section-title" style="top:2100px"><span>Our</span> Experience</h2>
  <div class="abs exp-intro">Kelvarn has a diverse range of project experience across a range of industries within both the public and private sectors.<br>The following is a small sample of some of the clients and sites we have worked with.</div>
  <svg class="abs arrow" style="left:46px" viewBox="0 0 20 30"><polyline points="15,5 5,15 15,25" fill="none" stroke="#888" stroke-width="3"/></svg>
  <svg class="abs arrow" style="left:1133px" viewBox="0 0 20 30"><polyline points="5,5 15,15 5,25" fill="none" stroke="#fff" stroke-width="3"/></svg>

  <article class="abs exp-card" style="left:111px">
    <div class="exp-img" role="img" aria-label="City skyline across a river at dusk" style="background:linear-gradient(180deg,#6f8fb8,#b28b6a 60%,#2a2a2a)"></div>
    <h3>Brindlewood Central</h3>
    <p>Security technology design<br>consulting for this popular retail and<br>entertainment hub which is managed<br>by the Pellmore Group.</p>
  </article>
  <article class="abs exp-card current" style="left:450px">
    <div class="exp-img" role="img" aria-label="City towers lit at night over water" style="background:linear-gradient(180deg,#1d3b8c,#2b4aa0 50%,#b7882a 75%,#141a2a)"></div>
    <h3>Corvane Towers</h3>
    <p>Shared building network and security<br>systems integration consulting for<br>this iconic office tower which is<br>managed by Haskett Property.</p>
  </article>
  <article class="abs exp-card" style="left:789px">
    <div class="exp-img" role="img" aria-label="Campus buildings in front of snowy mountains" style="background:linear-gradient(180deg,#c9d4e0,#8a97a8 35%,#4f6b3a 65%,#2e4a22)"></div>
    <h3>Ambervale Water</h3>
    <p>Critical Infrastructure Security Upgrade<br>for multiple water treatment sites<br>including perimeter fencing, CCTV,<br>access control &amp; electric keying.</p>
  </article>

  <section class="abs contact" role="img" aria-label="Red tinted city view with network lines"></section>
  <h2 class="abs section-title" style="top:2885px;font-size:40px">Get In Touch</h2>
  <div class="abs field" style="left:227px;top:2972px;width:367px;height:47px">Full Name</div>
  <div class="abs field" style="left:606px;top:2972px;width:367px;height:47px">Phone</div>
  <div class="abs field" style="left:227px;top:3032px;width:367px;height:47px">Email Address</div>
  <div class="abs field" style="left:606px;top:3032px;width:367px;height:47px">Subject</div>
  <div class="abs field area" style="left:227px;top:3092px;width:746px;height:90px">Message</div>
  <div class="abs submit">SUBMIT NOW</div>

  <svg class="abs" style="left:0;top:3300px" width="1200" height="479" viewBox="0 0 1200 479">
    <polygon points="0,177 300,5 1200,170 1200,479 0,479" fill="#070707"/>
    <polygon points="520,18 1200,150 1200,178 480,30" fill="#ffffff"/>
  </svg>
  <div class="abs brand" style="left:111px;top:3582px;font-size:46px;">
    <span class="brand-mark" style="width:42px;height:42px"></span>KELVARN
  </div>

  <div class="abs foot-head" style="left:435px">Quick Links</div>
  <div class="abs foot-link" style="left:435px;top:3529px"><span class="dot"></span>Home</div>
  <div class="abs foot-link" style="left:435px;top:3569px"><span class="dot"></span>Experience</div>
  <div class="abs foot-link" style="left:435px;top:3608px"><span class="dot"></span>Services</div>
  <div class="abs foot-link" style="left:435px;top:3648px"><span class="dot"></span>Team</div>
  <div class="abs foot-link" style="left:435px;top:3687px"><span class="dot"></span>About</div>

  <div class="abs foot-head" style="left:626px">Other Links</div>
  <div class="abs foot-link" style="left:626px;top:3529px"><span class="dot"></span>Contact</div>
  <div class="abs foot-link" style="left:626px;top:3569px"><span class="dot"></span>Sitemap</div>
  <div class="abs foot-link" style="left:626px;top:3608px"><span class="dot"></span>Terms of Services</div>
  <div class="abs foot-link" style="left:626px;top:3648px"><span class="dot"></span>Privacy Policy</div>

  <div class="abs foot-head" style="left:867px">Contact Info</div>
  <svg class="abs" style="left:867px;top:3530px" width="10" height="14" viewBox="0 0 10 14"><path d="M5 0a5 5 0 0 1 5 5c0 4-5 9-5 9S0 9 0 5a5 5 0 0 1 5-5z" fill="#e0231f"/><circle cx="5" cy="5" r="2" fill="#070707"/></svg>
  <div class="abs info-label" style="left:899px;top:3529px">Address:</div>
  <div class="abs info-text" style="left:899px;top:3549px">Level 2, 118 Harbour Street<br>Melbourne, VIC, 3000 Australia</div>
  <svg class="abs" style="left:867px;top:3608px" width="12" height="12" viewBox="0 0 24 24"><path d="M6.6 10.8a15 15 0 0 0 6.6 6.6l2.2-2.2a1 1 0 0 1 1-.25 11.4 11.4 0 0 0 3.6.57 1 1 0 0 1 1 1V20a1 1 0 0 1-1 1A17 17 0 0 1 3 4a1 1 0 0 1 1-1h3.5a1 1 0 0 1 1 1c0 1.25.2 2.45.57 3.57a1 1 0 0 1-.25 1z" fill="#e0231f"/></svg>
  <div class="abs info-label" style="left:899px;top:3606px">Phone:</div>
  <div class="abs info-text" style="left:899px;top:3627px">1300 555 018</div>
  <svg class="abs" style="left:867px;top:3666px" width="14" height="10" viewBox="0 0 14 10"><rect width="14" height="10" fill="#e0231f"/><polyline points="0,0 7,6 14,0" fill="none" stroke="#070707" stroke-width="1.2"/></svg>
  <div class="abs info-label" style="left:899px;top:3663px">Email:</div>
  <div class="abs info-text" style="left:899px;top:3684px">hello@kelvarn.example</div>

  <div class="abs divider"></div>
  <div class="abs copyright">© 2023 KELVARN SERVICES &nbsp;|&nbsp; All Rights Reserved</div>
</div>
</body>
</html>
```